Business Card Design Project

We require a business card template to cover basic contact information - our company logo, names of employees, title, mobile and email.
Updates

Target Market(s)

Corporate

Industry/Entity Type

Business

Font styles to use
Sans Serif

Requirements
Nice to have
• Thinking it would be great just to have the logo taking up approximately half the space (so it goes as far across the top of the card as possible) and then contact details in the lower half of the card. Keen just to use only the two colours in the logo, on a white background.
Should not have
• No fussy drawings

```html
<!DOCTYPE html>
<html lang="en">
<head>
<meta charset="utf-8">
<title>Larkmere Developments – Business Cards</title>
<link href="https://fonts.googleapis.com/css2?family=Open+Sans:wght@400;600&display=swap" rel="stylesheet">
<style>
  :root {
    --teal: #2aa6b4;
    --blue: #2f64ad;
    --ink: #222a33;
    --paper: #ffffff;
    --backdrop: #e9ebee;
    --rule: #d5d9de;
  }
  * { margin: 0; padding: 0; box-sizing: border-box; }
  html, body { width: 1200px; height: 900px; overflow: hidden; }
  body {
    background: var(--backdrop);
    font-family: "Open Sans", Arial, sans-serif;
    color: var(--ink);
    position: relative;
  }
  .card {
    position: absolute;
    left: 280px;
    width: 640px;
    height: 366px;
    background: var(--paper);
    overflow: hidden;
    box-shadow: 0 6px 18px rgba(0,0,0,0.12);
  }
  .card--back { top: 56px; }
  .card--front { top: 478px; }

  .wordmark {
    color: var(--teal);
    font-weight: 400;
    line-height: 1;
    letter-spacing: -1px;
    white-space: nowrap;
  }
  .wordmark__sub {
    display: block;
    color: var(--teal);
    font-weight: 400;
    letter-spacing: 0;
    text-align: right;
  }

  /* Back card */
  .card--back .edge-left {
    position: absolute; left: 0; bottom: 0; width: 12px; height: 150px; background: var(--blue);
  }
  .card--back .edge-right {
    position: absolute; right: 0; top: 0; width: 12px; height: 120px; background: var(--blue);
  }
  .card--back .wordmark {
    position: absolute; left: 60px; top: 80px; font-size: 78px;
  }
  .card--back .wordmark__sub { font-size: 24px; margin-top: 2px; }
  .card--back .person {
    position: absolute; left: 60px; bottom: 72px;
  }
  .contact-row {
    position: absolute; left: 60px; right: 36px; bottom: 36px;
    display: flex; justify-content: space-between; align-items: baseline;
    font-size: 15px; white-space: nowrap;
  }
  .contact-row .label { color: var(--blue); font-weight: 600; margin-right: 4px; }
  .person__name { color: var(--teal); font-weight: 600; font-size: 18px; line-height: 1.05; white-space: nowrap; }
  .person__title { color: var(--teal); font-size: 12px; line-height: 1.2; }

  /* Front card */
  .band {
    position: absolute; left: 0; right: 0; height: 14px; background: var(--blue);
  }
  .band--top { top: 0; }
  .band--bottom { bottom: 0; }
  .tab {
    position: absolute; left: 50%; width: 196px; height: 28px; margin-left: -98px;
    background: var(--teal); border-radius: 6px; border: 2px solid var(--paper);
  }
  .tab--top { top: 2px; }
  .tab--bottom { bottom: 2px; }
  .card--front .wordmark {
    position: absolute; left: 50px; top: 136px; font-size: 56px;
  }
  .card--front .wordmark__sub { font-size: 18px; }
  .divider {
    position: absolute; left: 345px; top: 90px; width: 1px; height: 170px;
    background: linear-gradient(var(--paper), var(--rule) 30%, var(--rule) 70%, var(--paper));
  }
  .details { position: absolute; left: 372px; top: 128px; }
  .details .person__name { font-size: 16px; }
  .details .person__title { font-size: 11px; }
  .details ul { list-style: none; margin-top: 26px; font-size: 13px; white-space: nowrap; }
  .details li { display: flex; align-items: center; gap: 10px; margin-bottom: 8px; }
  .details svg { width: 12px; height: 12px; fill: var(--blue); flex: none; }
</style>
</head>
<body>

  <section class="card card--back">
    <div class="edge-left"></div>
    <div class="edge-right"></div>
    <div class="wordmark">Larkmere<span class="wordmark__sub">developments</span></div>
    <div class="person">
      <div class="person__name">YOURNAME</div>
      <div class="person__title">president</div>
    </div>
    <div class="contact-row">
      <div><span class="label">P:</span>0000 000 000</div>
      <div><span class="label">M:</span>0000 000 000</div>
      <div><span class="label">E:</span>alex@larkmeredev.net</div>
    </div>
  </section>

  <section class="card card--front">
    <div class="band band--top"></div>
    <div class="tab tab--top"></div>
    <div class="wordmark">Larkmere<span class="wordmark__sub">developments</span></div>
    <div class="divider"></div>
    <div class="details">
      <div class="person__name">YOURNAME</div>
      <div class="person__title">president</div>
      <ul>
        <li>
          <svg viewBox="0 0 12 12" aria-hidden="true"><rect x="2" y="1" width="8" height="10" rx="1.5"/></svg>
          0000 000 000
        </li>
        <li>
          <svg viewBox="0 0 12 12" aria-hidden="true"><path d="M3 0h6a1 1 0 0 1 1 1v10a1 1 0 0 1-1 1H3a1 1 0 0 1-1-1V1a1 1 0 0 1 1-1zm0.5 1.5v8h5v-8z"/></svg>
          0000 000 000
        </li>
        <li>
          <svg viewBox="0 0 12 12" aria-hidden="true"><rect x="0" y="2" width="12" height="8" rx="1"/></svg>
          yourmail@mailbox.com
        </li>
      </ul>
    </div>
    <div class="band band--bottom"></div>
    <div class="tab tab--bottom"></div>
  </section>

</body>
</html>
```